New Web-Page Design Required

We need a new or initial web design for our page korvel-net.com. We provide products & services around infrastructure products. We have two products at the moment, but another 2 in the pipeline.
We want to have the following page structure (and part of the project is to design the 7 pages):
- Home
- Products
-One page per product
- Service
- Support
- About
- Contact (Email form)
The start page should include the following information:
- Chirply / Workmesh Links
- Telephone / Email or in general contact details
- News
- Maybe a link-box, where we can highlight/showcase things
- Link to our support portal, quite prominent
- Testimonials
It would be nice if the product pages would have a image header, where we can put up a screenshot or something. Links to datasheet and videos of the product would be nice as well.
We like the "big banner in the middle" designs, like these two Vendra examples. No need to copy them, it should just give you an idea.
http://www.plomdesigns.com/itempreview/185
http://www.plomdesigns.com/content/pdk42/index.php
Budget for images available, so please use placeholders or ask us for specific photos/images, if you need them for your design.
Target Market(s)
Business-2-Business, Decision makers and Technical Leads
Industry/Entity Type
News
Look and feel
Each slider illustrates characteristics of the customer's brand and the style your logo design should communicate.

```html
<!DOCTYPE html>
<html lang="en">
<head>
<meta charset="utf-8">
<title>korvel net – Home</title>
<link rel="stylesheet" href="https://fonts.googleapis.com/css2?family=Open+Sans:wght@400;600&display=swap">
<style>
:root{
  --teal:#04a9bf;
  --page:#efefef;
  --header:#f2f2f2;
  --text:#333;
  --card:#fff;
  --footer:#333;
}
*{margin:0;padding:0;box-sizing:border-box}
html,body{width:1200px;height:1129px;overflow:hidden}
body{font-family:"Open Sans",sans-serif;background:var(--page);color:var(--text);position:relative}
a{color:inherit;text-decoration:none}

.topbar{position:absolute;top:0;left:0;width:1200px;height:48px;background:var(--teal);color:#fff;font-size:16px}
.topbar .contact{position:absolute;top:13px;display:flex;align-items:center;gap:12px}
.topbar .mail{left:130px}
.topbar .phone{left:350px}
.search{position:absolute;left:854px;top:11px;width:216px;height:26px;background:#fff;border:1px solid #dcdcdc;font-size:9px;color:#aaa;padding:6px 8px}
.search svg{position:absolute;right:6px;top:6px}

.site-header{position:absolute;top:48px;left:0;width:1200px;height:90px;background:var(--header)}
.brand{position:absolute;left:130px;top:24px;font-size:34px;font-weight:600;color:var(--teal);letter-spacing:-1px}
.main-nav{position:absolute;right:130px;top:36px;display:flex;gap:32px;font-size:16px;color:#444}
.main-nav .active{color:var(--teal)}

.hero{position:absolute;top:138px;left:0;width:1200px;height:362px;background:linear-gradient(100deg,#d6d6d6 0%,#e9e9e9 55%,#dcdcdc 100%)}
.hero h1{position:absolute;left:130px;top:120px;font-size:33px;font-weight:400;color:var(--teal)}
.hero p{position:absolute;left:130px;top:168px;font-size:12.6px;line-height:22px;color:#333}
.pager{position:absolute;left:130px;top:290px;display:flex;gap:3px}
.pager span{width:13px;height:13px;border-radius:50%;background:#333}
.pager span.on{background:#fff;border:2px solid #333}
.tablet{position:absolute;left:677px;top:33px;width:372px;height:293px;border-radius:18px;background:#111;border:3px solid #bbb;box-shadow:0 14px 18px -14px rgba(0,0,0,.5)}
.tablet .screen{position:absolute;left:23px;top:24px;width:322px;height:242px;background:linear-gradient(160deg,#3a3a3a,#1e1e1e 60%,#2b3a3e)}

.card{position:absolute;top:516px;height:312px;background:var(--card);border-radius:4px;overflow:hidden}
.card-head{height:43px;background:var(--teal);color:#fff;font-size:17.5px;padding:10px 26px;position:relative}
.card-head .arrows{position:absolute;right:18px;top:17px;display:flex;gap:10px}
.card-body{padding:0 26px;font-size:12.6px;line-height:20px;color:#444;text-align:justify;letter-spacing:-0.1px}
.highlights{left:130px;width:300px}
.support{left:451px;width:300px}
.news{left:770px;width:300px}
.shot{width:172px;height:127px;margin:17px auto 17px;background:linear-gradient(180deg,#3a3a3a,#222)}
.photo{width:110px;height:142px;margin:13px auto 6px;background:linear-gradient(180deg,#e9e4e0,#cfc6c0)}
.portal-btn{display:block;width:200px;height:27px;margin:10px auto 0;background:var(--teal);color:#fff;text-align:center;font-size:12.6px;line-height:27px}
.news .card-body{padding-top:52px;padding-left:28px;text-align:left}
.news h3{font-size:12.6px;font-weight:600;color:#333}
.news .date{margin-bottom:20px}
.news .summary{text-align:justify}

.testimonials{position:absolute;top:858px;left:130px;width:940px;text-align:center}
.testimonials h2{font-size:16.5px;font-weight:400;color:var(--teal);padding-bottom:4px;border-bottom:1px solid #ddd}
.testimonials blockquote{margin-top:15px;font-size:12.4px;line-height:20px;color:#333;letter-spacing:-0.1px}
.testimonials cite{display:block;margin-top:12px;font-style:normal;font-weight:600;font-size:12.6px}

.site-footer{position:absolute;top:1043px;left:0;width:1200px;height:86px;background:var(--footer);color:#fff;font-size:12.6px}
.footer-nav{position:absolute;left:130px;top:20px;display:flex;gap:14px}
.footer-nav .sep{color:#ccc}
.copy{position:absolute;left:130px;top:46px}
.social{position:absolute;right:130px;top:33px;display:flex;gap:14px;align-items:center}
.social a{display:flex;align-items:center;gap:5px}
.social .dot{width:14px;height:14px;border-radius:50%;background:#fff}
</style>
</head>
<body>

<div class="topbar">
  <div class="contact mail">
    <svg width="28" height="20" viewBox="0 0 28 20"><rect x="1" y="1" width="26" height="18" fill="none" stroke="#333" stroke-width="2"/><path d="M1 1l13 10L27 1" fill="none" stroke="#333" stroke-width="2"/></svg>
    <span>info@korvel-net.com</span>
  </div>
  <div class="contact phone">
    <svg width="16" height="22" viewBox="0 0 16 22"><path d="M3 1h4l1 5-3 2c1 3 3 6 5 8l3-2 3 4-3 3C6 19 1 10 3 1z" fill="#333"/></svg>
    <span>1800-555-017-42</span>
  </div>
  <div class="search">Type search
    <svg width="12" height="12" viewBox="0 0 12 12"><circle cx="5" cy="5" r="3.5" fill="none" stroke="#999"/><path d="M7.5 7.5l3.5 3.5" stroke="#999" stroke-width="1.5"/></svg>
  </div>
</div>

<header class="site-header">
  <div class="brand">korvel net</div>
  <nav class="main-nav">
    <a class="active" href="#">Home</a><a href="#">Products</a><a href="#">Services</a><a href="#">Support</a><a href="#">Contact</a>
  </nav>
</header>

<section class="hero">
  <h1>Tarvo OS Coming Soon!</h1>
  <p>A Tarvo OS version of q.Dash for Netvigil® will be released in August.<br>You will see the same great features as in the Quilla OS version.</p>
  <div class="pager"><span class="on"></span><span></span><span></span><span></span></div>
  <div class="tablet"><div class="screen" role="img" aria-label="Screenshot of the q.Dash monitoring app showing availability and memory charts"></div></div>
</section>

<section class="card highlights">
  <div class="card-head">Product Highlights
    <span class="arrows"><svg width="8" height="14"><path d="M7 1L1 7l6 6" fill="none" stroke="#fff" stroke-width="2"/></svg><svg width="8" height="14"><path d="M1 1l6 6-6 6" fill="none" stroke="#fff" stroke-width="2"/></svg></span>
  </div>
  <div class="shot" role="img" aria-label="Product screenshot of the device summary dashboard"></div>
  <p class="card-body">Our understanding for customer needs combined with our software development experience, enables us to provide products of outstanding quality.</p>
</section>

<section class="card support">
  <div class="card-head">Our Support</div>
  <div class="photo" role="img" aria-label="Photo of a support agent wearing a headset"></div>
  <p class="card-body">Our support portal is available 24/7 and personalized support packages can be tailored to your needs.</p>
  <a class="portal-btn" href="#">Click here to Support Portal</a>
</section>

<section class="card news">
  <div class="card-head">Latest News
    <span class="arrows"><svg width="8" height="14"><path d="M7 1L1 7l6 6" fill="none" stroke="#fff" stroke-width="2"/></svg><svg width="8" height="14"><path d="M1 1l6 6-6 6" fill="none" stroke="#fff" stroke-width="2"/></svg></span>
  </div>
  <div class="card-body">
    <h3>VRD/C Released</h3>
    <p class="date">2013-05-21</p>
    <p class="summary">Korvel-Net has released the first version of the Vireo Cloud Director Collector for Emvara Netvigil. The collector is natively integrated into the Netvigil installation and comes with a rich set of reports.</p>
  </div>
</section>

<section class="testimonials">
  <h2>Testimonials</h2>
  <blockquote>"Lorem Ipsum is simply dummy text of the printing and typesetting industry. Lorem Ipsum has been the industry's standard dummy text ever since the 1500s, when an unknown printer took a galley of type and scrambled it to make a type specimen book. It has survived not only five centuries, but also the leap into electronic typesetting, remaining essentially unchanged. "</blockquote>
  <cite>- Dana Holloway, McKinney, Texas</cite>
</section>

<footer class="site-footer">
  <nav class="footer-nav">
    <a href="#">Home</a><span class="sep">|</span><a href="#">Products</a><span class="sep">|</span><a href="#">Services</a><span class="sep">|</span><a href="#">Support</a><span class="sep">|</span><a href="#">Contact</a>
  </nav>
  <p class="copy">©2013 korvel net | All Rights Reserved</p>
  <div class="social">
    <a href="#"><span class="dot"></span>Chirply</a>
    <a href="#"><span class="dot"></span>Workmesh</a>
  </div>
</footer>

</body>
</html>
```